We are “Velvet Coachline” a Chauffeur Company based in Maidenhead, Berkshire. Our website is - velvetcoachline.co.uk which will give you an insite into the Company.
Our clients consist of luxurious Hotels, large Corporate Companies along with private UHNW clients.
We have a fleet of Valtrane E, S and V Class vehicles along with 16 Seater Executive Coaches so we can accommodate single travellers, couples, friends, families and groups.
We would like an A5 (or slightly larger) double sided colour leaflet designed to promote our Tours in our local and surrounding areas.
The information below is some indication as to what we would like.
On the front we would like:-
Velvet Coachline “Heritage Circuit” This will be our main promoting Tour
Slogan “Velvet Coachline….forever at your call”
Tour will include:-
Visiting the historic town of Windsor, Harrowmere Keep, Linden Abbey Chapel and Grand Fenwick Trading Gallery.
Then onto Eton (Ashcombe Academy) and a lovely view of the River Thames along with an array of Antique Shops in the quaint streets.
Bray Village (Heron Eyot), renowed for it’s Michelin Star Restaurants and pubs.
Through picturesque Cookham along to Marlow for some shopping in the boutique shops, small listed buildings and beautiful places for refreshments, along with stunning views of the River Thames form Marlow Bridge.
This will be our main tour we offer but again this is flexible. This aims to be around 4-5 hours.
On the front, a picture of Harrowmere keep maybe a large picture with writing over the top, or a separate photo….. a couple of photos attached or something similar.
On the back of the leaflet:-
We offer London based tours including:-
Pellbury’s, Corran Fields, Alderwick Palace, Thornleigh Palace, Pemberly Plaza, Turning of the Sentries, Greystone Fortress, Tall Tom, Kelbourne Minster to name a few! Or maybe London by night with a show or restaurant.
On the back a picture of Thornleigh Palace…a couple of picture are also attached or again something similar.
Other Tours provided:-
Dunmere Hall Palace, Oxford and Corravin Palace, Ravenring and Bath, The Cotswolds, Stratford and Fellbrook Castle, Quillmoor Outlet Village.
Also bespoke Tours can be arranged. We can personalise any tour to your requirements.
Experienced friendly Chauffeur’s, no request too big or small.
Please call us on 01632 960417 or email us sales@velvetcoachline.co.uk
Please can you do an initial design including the above information.
Look forward to hearing from you.
Kind regards
Please visit https://www.brackenlimousines.co.uk/ to get an idea of the tours of London to go on the back.
Prices will follow to be added after design and layout has been done.
Our VC logo is available on www.velvetcoachline.co.uk
We want text to be editable and also for the design to have a luxury feel.

```html
<!DOCTYPE html>
<html lang="en">
<head>
<meta charset="utf-8">
<title>Velvet Coachline – London &amp; Other Tours</title>
<link rel="stylesheet" href="https://fonts.googleapis.com/css2?family=Raleway:wght@400;500;600&family=Open+Sans:wght@400;700&display=swap">
<style>
  :root {
    --ink: #1d1d1d;
    --ink-deep: #141414;
    --ink-band: #181818;
    --gold: #b8963e;
    --gold-soft: #c9ae62;
    --gold-dark: #3d2d0c;
    --edge-red: #4a1410;
    --white: #ffffff;
  }
  html, body {
    margin: 0;
    padding: 0;
    overflow: hidden;
    background: var(--ink);
  }
  .leaflet-back {
    position: relative;
    width: 846px;
    height: 1200px;
    overflow: hidden;
    background: var(--ink);
    color: var(--white);
    font-family: "Raleway", sans-serif;
  }
  .backdrop {
    position: absolute;
    inset: 0;
  }
  .section-title {
    position: absolute;
    margin: 0;
    font-family: "Raleway", sans-serif;
    font-weight: 600;
    font-size: 21px;
    letter-spacing: 1.9px;
    line-height: 1;
  }
  .london-title { left: 57px; top: 61px; }
  .other-title { left: 100px; top: 765px; }
  .tour-list {
    position: absolute;
    margin: 0;
    font-weight: 400;
    font-size: 21.5px;
    line-height: 26.7px;
    white-space: nowrap;
  }
  .london-list { left: 57px; top: 104px; }
  .other-list { left: 115px; top: 808px; }
  .other-list .line-2 { padding-left: 5px; }
  .other-list .line-3 { padding-left: 17px; }
  .feature {
    position: absolute;
    margin: 0;
    font-size: 21.5px;
    line-height: 26.7px;
    white-space: nowrap;
    padding-left: 17px;
    text-indent: -17px;
  }
  .feature::before { content: "» "; font-size: 18px; }
  .feature-bespoke { left: 150px; top: 915px; }
  .feature-chauffeur { left: 185px; top: 995px; }
  .contact-panel {
    position: absolute;
    left: 286px;
    top: 1091px;
    width: 560px;
    height: 84px;
  }
  .contact-text {
    position: absolute;
    right: 39px;
    top: 1104px;
    margin: 0;
    text-align: right;
    font-family: "Open Sans", sans-serif;
    font-size: 22px;
    line-height: 28px;
    white-space: nowrap;
  }
  .contact-text .first { padding-right: 64px; display: inline-block; }
  .contact-phone { color: var(--gold-soft); font-weight: 700; }
  .contact-email { font-weight: 700; }
</style>
</head>
<body>
<main class="leaflet-back">
  <svg class="backdrop" width="846" height="1200" viewBox="0 0 846 1200" aria-hidden="true">
    <polygon points="642,0 846,0 846,240 742,270" fill="var(--ink-deep)"/>
    <line x1="642" y1="0" x2="742" y2="270" stroke="var(--edge-red)" stroke-width="1.5"/>
    <line x1="760" y1="0" x2="846" y2="230" stroke="var(--edge-red)" stroke-width="1.5"/>
    <polygon points="0,710 30,710 205,1200 0,1200" fill="var(--ink-deep)"/>
    <line x1="30" y1="720" x2="205" y2="1200" stroke="var(--gold-dark)" stroke-width="1.5"/>
    <polygon points="0,950 90,1200 0,1200" fill="var(--ink-band)"/>
    <line x1="0" y1="950" x2="90" y2="1200" stroke="#2a2a2a" stroke-width="1"/>
  </svg>

  <h2 class="section-title london-title">WE OFFER LONDON BASED TOURS INCLUDING:</h2>
  <p class="tour-list london-list">
    Pellbury’s, Corran Fields, Alderwick Palace, Thornleigh<br>
    Palace, Pemberly Plaza, Turning of the Sentries,<br>
    Greystone Fortress, Tall Tom, Kelbourne Minster to name<br>
    a few! Or maybe London by night with a show or restaurant.
  </p>

  <svg class="backdrop" width="846" height="1200" viewBox="0 0 846 1200">
    <path d="M0,287 Q423,245 846,287 L846,703 Q423,749 0,703 Z" fill="var(--gold)"/>
    <path d="M0,299 Q423,255 846,299 L846,693 Q423,735 0,693 Z" fill="var(--ink)"/>
    <defs>
      <linearGradient id="palace-scene" x1="0" y1="0" x2="0" y2="1">
        <stop offset="0" stop-color="#3f82d6"/>
        <stop offset="0.35" stop-color="#7fb0e6"/>
        <stop offset="0.5" stop-color="#d8d4c8"/>
        <stop offset="0.72" stop-color="#bfae5a"/>
        <stop offset="0.85" stop-color="#d9c23a"/>
        <stop offset="1" stop-color="#c8261c"/>
      </linearGradient>
    </defs>
    <path role="img" aria-label="Photograph of Thornleigh Palace with its memorial and spring tulip beds in the foreground"
          d="M0,299 Q423,255 846,299 L846,693 Q423,735 0,693 Z" fill="url(#palace-scene)"/>
  </svg>

  <h2 class="section-title other-title">OTHER TOURS PROVIDED:</h2>
  <p class="tour-list other-list">
    <span class="line-1">Dunmere Hall Palace, Oxford and Corravin Palace,</span><br>
    <span class="line-2">Ravenring and Bath, The Cotswolds, Stratford and</span><br>
    <span class="line-3">Fellbrook Castle, Quillmoor Outlet Village.</span>
  </p>

  <p class="feature feature-bespoke">Also bespoke Tours can be arranged. We can personalise<br>any tour to your requirements.</p>
  <p class="feature feature-chauffeur">Experienced friendly Chauffeur’s, no request too big<br>or small.</p>

  <svg class="contact-panel" viewBox="0 0 560 84" aria-hidden="true">
    <polygon points="2,2 560,2 560,82 28,82" fill="var(--gold-dark)" stroke="var(--gold)" stroke-width="3"/>
  </svg>
  <p class="contact-text">
    <span class="first">Please call us on <span class="contact-phone">01632 960417</span></span><br>
    or email us <span class="contact-email">sales@velvetcoachline.co.uk</span>
  </p>
</main>
</body>
</html>
```